LED strip light bag design

We are brivexa lighting, a LED strip manufacturer in China, We need a packaging design for our LED strip light, as the strip market is full of standard package, so we want to make our package special, and use color orange, black and grey

Target Market(s)

USA, Europe

Contact Information for Business Card

Morgan Pidd
Director
Shenzhen Brivexa Lighting Co., Ltd.
Add: 3F, Gaotang Ind. Zone, Wenhu Rd, Liaobu, Shenzhen 518392 China
Tel: +86-139-4086 3827 Fax: +86-755-29483066
E-mail: morgan.pidd@brivexa-example.com

Font styles to use
Sans Serif
Other font styles liked:
• Tw Cen MT Condensed

Colors

Designer to choose only greyscale colors for use in the design.

Requirements
Must have
• Must have instructions of how to use the strip and CAUTION
• Must have CE, RoHS UL, trash can, ISO9001 logo
Nice to have
• Nice to have a back ground pictures with a strip drawing.

```html
<!DOCTYPE html>
<html lang="en">
<head>
<meta charset="utf-8">
<title>Brivexa LED Strip Light Bag</title>
<link rel="stylesheet" href="https://fonts.googleapis.com/css2?family=Saira+Condensed:wght@400;600;700&family=Pathway+Gothic+One&display=swap">
<style>
  :root {
    --orange: #f7941d;
    --orange-deep: #f15a24;
    --orange-light: #fbb03b;
    --black: #231f20;
    --white: #ffffff;
    --ink: #231f20;
  }
  html, body {
    margin: 0;
    padding: 0;
    width: 1200px;
    height: 706px;
    overflow: hidden;
    background: var(--white);
  }
  .bag-artwork {
    display: block;
    width: 1200px;
    height: 706px;
  }
  .brand-name {
    font-family: "Saira Condensed", sans-serif;
    font-weight: 700;
    font-size: 40px;
    fill: var(--white);
  }
  .product-title {
    font-family: "Saira Condensed", sans-serif;
    font-weight: 400;
    font-size: 104px;
    fill: var(--white);
  }
  .product-tagline {
    font-family: "Saira Condensed", sans-serif;
    font-weight: 700;
    font-size: 31px;
    fill: var(--white);
  }
  .instructions-label {
    font-family: "Pathway Gothic One", sans-serif;
    font-size: 30px;
    fill: var(--ink);
  }
  .caution-heading {
    font-family: "Pathway Gothic One", sans-serif;
    font-size: 19px;
    fill: var(--ink);
  }
  .caution-sub {
    font-family: "Pathway Gothic One", sans-serif;
    font-size: 11.5px;
    fill: var(--ink);
  }
  .caution-item {
    font-family: "Pathway Gothic One", sans-serif;
    font-size: 9.5px;
    fill: var(--ink);
  }
</style>
</head>
<body>
<svg class="bag-artwork" viewBox="0 0 1500 882" xmlns="http://www.w3.org/2000/svg">
  <defs>
    <radialGradient id="burst-field" cx="0.02" cy="0.02" r="1.2">
      <stop offset="0" stop-color="var(--orange-light)"/>
      <stop offset="0.5" stop-color="var(--orange)"/>
      <stop offset="1" stop-color="#f58220"/>
    </radialGradient>
    <radialGradient id="dot-glow" cx="0.5" cy="0.5" r="0.5">
      <stop offset="0" stop-color="#6d6e71" stop-opacity="0.55"/>
      <stop offset="1" stop-color="#6d6e71" stop-opacity="0"/>
    </radialGradient>
  </defs>

  <!-- Bag background -->
  <rect class="bag-field" x="22" y="24" width="1456" height="834" fill="url(#burst-field)"/>

  <!-- Black face panel -->
  <polygon class="face-panel" fill="var(--black)"
    points="322,24 1178,24 1260,180 900,858 600,858 240,180"/>

  <!-- Diagonal orange bands -->
  <polygon class="side-band" fill="var(--orange-deep)"
    points="262,24 322,24 240,180 600,858 485,858 212,315 212,125"/>
  <polygon class="side-band" fill="var(--orange-deep)"
    points="1238,24 1178,24 1260,180 900,858 1015,858 1288,315 1288,125"/>

  <line class="fold-line" x1="750" y1="24" x2="750" y2="858" stroke="#3a3a3a" stroke-width="1"/>

  <!-- Halftone backdrop area -->
  <g role="img" aria-label="Grey dotted halftone swirl pattern behind the title">
    <ellipse cx="560" cy="420" rx="150" ry="230" fill="url(#dot-glow)"/>
    <ellipse cx="940" cy="420" rx="150" ry="230" fill="url(#dot-glow)"/>
  </g>

  <!-- Brand marks -->
  <g class="brand front-left">
    <circle cx="461" cy="192" r="15" fill="var(--orange)"/>
    <text class="brand-name" x="484" y="205">BRIVEXA</text>
  </g>
  <g class="brand front-right">
    <circle cx="834" cy="192" r="15" fill="var(--orange)"/>
    <text class="brand-name" x="857" y="205">BRIVEXA</text>
  </g>

  <!-- Left face titles -->
  <text class="product-title" transform="translate(330,228) rotate(60)" textLength="630" lengthAdjust="spacingAndGlyphs">LED STRIP LIGHT</text>
  <text class="product-tagline" transform="translate(276,365) rotate(62)" textLength="440" lengthAdjust="spacingAndGlyphs">EASY TO USE LED STRIP LIGHTNING</text>

  <!-- Right face titles -->
  <text class="product-title" transform="translate(850,778) rotate(-60)" textLength="630" lengthAdjust="spacingAndGlyphs">LED STRIP LIGHT</text>
  <text class="product-tagline" transform="translate(1019,758) rotate(-62)" textLength="440" lengthAdjust="spacingAndGlyphs">EASY TO USE LED STRIP LIGHTNING</text>

  <!-- Back: instructions -->
  <text class="instructions-label" x="110" y="690">INSTRUCTIONS</text>

  <!-- Back: caution box -->
  <g class="caution-box">
    <rect x="1201" y="539" width="248" height="218" rx="12" fill="none" stroke="var(--ink)" stroke-width="1.4"/>
    <text class="caution-heading" x="1325" y="562" text-anchor="middle">CAUTION</text>
    <text class="caution-sub" x="1325" y="578" text-anchor="middle">THIS BAG CONTAINS MOISTURE</text>
    <text class="caution-sub" x="1325" y="594" text-anchor="middle">AND ELECTROSTATIC SENSITIVE DEVICES.</text>
    <text class="caution-item" x="1214" y="624">Attention</text>
    <text class="caution-item" x="1214" y="637">1. Storage Temperature:- 40 ~ +80°C</text>
    <text class="caution-item" x="1222" y="650">Operating Temperature:- 25 ~ +60°C</text>
    <text class="caution-item" x="1214" y="663">2. Installation surface must be smooth, clean and dry.</text>
    <text class="caution-item" x="1214" y="676">3. The part of LED components can not be fixed on the surface</text>
    <text class="caution-item" x="1222" y="689">of the sharp edge.</text>
    <text class="caution-item" x="1214" y="702">4. Strip should not be collided or crushed.</text>
    <text class="caution-item" x="1214" y="715">5. Strip can be cut following the cutting lines.</text>
    <text class="caution-item" x="1214" y="728">6. The led strips must not exceed 5 meters, when used in a</text>
    <text class="caution-item" x="1222" y="741">DC series circuit.</text>
  </g>

  <!-- Back: certification badges -->
  <g class="cert-badges" fill="var(--ink)">
    <rect x="1188" y="778" width="40" height="26" rx="3"/>
    <rect x="1240" y="778" width="68" height="26" rx="3"/>
    <circle cx="1332" cy="791" r="14"/>
    <rect x="1354" y="778" width="20" height="26" rx="2"/>
    <circle cx="1397" cy="791" r="15"/>
    <polygon points="1414,778 1462,778 1452,804 1414,804"/>
  </g>
</svg>
</body>
</html>
```